Weight Loss Challenge Social Media Graphics

Create 6-7 individual social media graphics (square size) to encourage folks to join our weight loss challenge. For the color scheme of the graphics, use the color palette attached

Note: each graphic can contain any of the stock photography attached or just the single picture of me (brown shirt) but a few should be ONLY the text
For some graphics we can say: JOIN US!
For some graphics, use only TEXT based

Target Market(s)

primarily women who want to get healthy

Industry/Entity Type

health and weight loss

Requirements
Must have
• The largest text should be: Ninety Days Bold

```html
<!DOCTYPE html>
<html lang="en">
<head>
<meta charset="utf-8">
<title>Ninety Days Bold – Challenge Social Graphics</title>
<link rel="stylesheet" href="https://fonts.googleapis.com/css2?family=Archivo+Black&family=Montserrat:wght@300;400;700&display=swap">
<style>
  :root {
    --page: #ffffff;
    --mauve: #b08a84;
    --mauve-dark: #9c756f;
    --cream: #f3ddd0;
    --blush: #ffd3e8;
    --pink: #ff9bd4;
    --hot-pink: #f77ccd;
    --glow: #ff5fbf;
    --white: #ffffff;
    --paper: #ececec;
    --paper-dark: #dcdcdc;
  }
  * { box-sizing: border-box; margin: 0; padding: 0; }
  html, body { width: 1200px; height: 874px; overflow: hidden; background: var(--page); }
  .board { position: relative; width: 1200px; height: 874px; }

  .tile { position: absolute; width: 355px; height: 355px; overflow: hidden; background: var(--mauve); }
  .tile--a { left: 25px;  top: 57px; }
  .tile--b { left: 422px; top: 57px; }
  .tile--c { left: 819px; top: 57px; }
  .tile--d { left: 25px;  top: 456px; }
  .tile--e { left: 422px; top: 456px; background: linear-gradient(135deg, var(--paper), var(--paper-dark) 60%, var(--paper)); }
  .tile--f { left: 819px; top: 456px; background: var(--hot-pink); }

  .t {
    position: absolute; transform: translate(-50%, -50%);
    white-space: nowrap; line-height: 1; text-align: center; color: var(--white);
  }
  .heavy { font-family: "Archivo Black", "Arial Black", sans-serif; }
  .light { font-family: "Montserrat", Arial, sans-serif; font-weight: 300; }
  .bold  { font-family: "Montserrat", Arial, sans-serif; font-weight: 700; }
  .glow-pink { color: var(--blush); text-shadow: 0 0 4px var(--glow), 0 0 9px var(--glow); }
  .pink { color: var(--pink); }
  .soft-shadow { text-shadow: 0 1px 3px rgba(0,0,0,.25); }

  .photo { position: absolute; }
  .frame { position: absolute; background: var(--cream); }
  .rule { position: absolute; height: 3px; background: var(--cream); }

  .dot-rule { position: absolute; height: 2px; }
  .dot-rule::before, .dot-rule::after {
    content: ""; position: absolute; top: -2px; width: 6px; height: 6px; border-radius: 50%; background: inherit;
  }
  .dot-rule::before { left: -3px; } .dot-rule::after { right: -3px; }

  .band { position: absolute; left: 0; right: 0; top: 60px; height: 235px; background: var(--mauve); }
  .device { position: absolute; left: 2px; top: 25px; width: 150px; height: 307px; }
</style>
</head>
<body>
<main class="board">

  <!-- Graphic 1: two group photos -->
  <section class="tile tile--a">
    <div class="t heavy glow-pink" style="left:178px;top:23px;font-size:21px;">BOLD START CHALLENGE</div>
    <div class="frame" style="left:196px;top:45px;width:6px;height:270px;"></div>
    <div class="photo" role="img" aria-label="Four smiling women in sports bras and leggings posing together" style="left:0;top:45px;width:198px;height:136px;background:linear-gradient(135deg,#c9d8c8,#b8a2a6 60%,#d9c3c3);"></div>
    <div class="photo" role="img" aria-label="Cheerful group of adults flexing their arms in a gym" style="left:0;top:185px;width:198px;height:129px;background:linear-gradient(135deg,#a9c4e6,#c79a86 55%,#e7d5cf);"></div>
    <div class="rule" style="left:206px;top:53px;width:127px;"></div>
    <div class="rule" style="left:206px;top:300px;width:127px;"></div>
    <div class="t light soft-shadow" style="left:268px;top:73px;font-size:14px;letter-spacing:1px;">NINETY DAYS</div>
    <div class="t heavy glow-pink" style="left:268px;top:100px;font-size:36px;">BOLD</div>
    <div class="t light soft-shadow" style="left:268px;top:136px;font-size:37px;">LOSE</div>
    <div class="t light soft-shadow" style="left:268px;top:168px;font-size:25px;">UP TO 20</div>
    <div class="t light soft-shadow" style="left:268px;top:193px;font-size:19px;">POUNDS IN</div>
    <div class="t heavy glow-pink" style="left:266px;top:229px;font-size:53px;">SIX</div>
    <div class="t light soft-shadow" style="left:268px;top:276px;font-size:32px;">WEEKS</div>
    <div class="t heavy glow-pink" style="left:178px;top:335px;font-size:17px;letter-spacing:1px;">BEGINS 6 JANUARY 2025</div>
  </section>

  <!-- Graphic 2: single sign photo -->
  <section class="tile tile--b">
    <div class="t heavy glow-pink" style="left:182px;top:23px;font-size:21px;">BOLD START CHALLENGE</div>
    <div class="frame" style="left:0;top:45px;width:205px;height:270px;"></div>
    <div class="photo" role="img" aria-label="Woman in leggings holding a cardboard weight loss sign in front of her" style="left:0;top:52px;width:196px;height:254px;background:linear-gradient(180deg,#efece8,#d9c3a0 40%,#7d8fa0 80%,#eeeeee);"></div>
    <div class="rule" style="left:205px;top:53px;width:128px;"></div>
    <div class="rule" style="left:205px;top:300px;width:128px;"></div>
    <div class="t light soft-shadow" style="left:268px;top:73px;font-size:14px;letter-spacing:1px;">NINETY DAYS</div>
    <div class="t heavy glow-pink" style="left:268px;top:100px;font-size:36px;">BOLD</div>
    <div class="t light soft-shadow" style="left:268px;top:136px;font-size:37px;">LOSE</div>
    <div class="t light soft-shadow" style="left:268px;top:168px;font-size:25px;">UP TO 20</div>
    <div class="t light soft-shadow" style="left:268px;top:193px;font-size:19px;">POUNDS IN</div>
    <div class="t heavy glow-pink" style="left:266px;top:229px;font-size:53px;">SIX</div>
    <div class="t light soft-shadow" style="left:268px;top:276px;font-size:32px;">WEEKS</div>
    <div class="t heavy glow-pink" style="left:178px;top:335px;font-size:17px;letter-spacing:1px;">BEGINS 6 JANUARY 2025</div>
  </section>

  <!-- Graphic 3: two studio group photos -->
  <section class="tile tile--c">
    <div class="t heavy glow-pink" style="left:182px;top:23px;font-size:21px;">BOLD START CHALLENGE</div>
    <div class="frame" style="left:200px;top:45px;width:5px;height:280px;"></div>
    <div class="photo" role="img" aria-label="Group of women of different ages in black bodysuits posing in a studio" style="left:0;top:45px;width:200px;height:138px;background:linear-gradient(135deg,#8a6250,#5a3d30 50%,#8f6a58);"></div>
    <div class="frame" style="left:0;top:183px;width:205px;height:4px;"></div>
    <div class="photo" role="img" aria-label="Group of smiling women in sports tops hugging in a studio" style="left:3px;top:187px;width:197px;height:138px;background:linear-gradient(135deg,#9a7261,#6d4a3b 50%,#a98472);"></div>
    <div class="rule" style="left:206px;top:53px;width:128px;"></div>
    <div class="rule" style="left:206px;top:300px;width:128px;"></div>
    <div class="t light soft-shadow" style="left:268px;top:73px;font-size:14px;letter-spacing:1px;">NINETY DAYS</div>
    <div class="t heavy glow-pink" style="left:268px;top:100px;font-size:36px;">BOLD</div>
    <div class="t light soft-shadow" style="left:268px;top:136px;font-size:37px;">LOSE</div>
    <div class="t light soft-shadow" style="left:268px;top:168px;font-size:25px;">UP TO 20</div>
    <div class="t light soft-shadow" style="left:268px;top:193px;font-size:19px;">POUNDS IN</div>
    <div class="t heavy glow-pink" style="left:266px;top:229px;font-size:53px;">SIX</div>
    <div class="t light soft-shadow" style="left:268px;top:276px;font-size:32px;">WEEKS</div>
    <div class="t heavy glow-pink" style="left:178px;top:340px;font-size:17px;letter-spacing:1px;">BEGINS 6 JANUARY 2025</div>
  </section>

  <!-- Graphic 4: phone with couple photo, mauve -->
  <section class="tile tile--d">
    <svg class="device" viewBox="0 0 150 307" aria-hidden="true">
      <rect x="1" y="1" width="148" height="305" rx="22" fill="#f4f4f4" stroke="#cfcfcf" stroke-width="2"/>
      <circle cx="52" cy="19" r="2.5" fill="#333"/>
      <rect x="62" y="17" width="28" height="3" rx="1.5" fill="#444"/>
      <circle cx="73" cy="286" r="11" fill="none" stroke="#9a9a9a" stroke-width="2"/>
    </svg>
    <div class="photo" role="img" aria-label="Fit man and woman at the beach measuring their waists with tape" style="left:9px;top:54px;width:138px;height:241px;background:linear-gradient(180deg,#b9cde3,#c9a48c 45%,#6f6f73 80%,#9ea0a5);"></div>
    <div class="t heavy pink" style="left:258px;top:23px;font-size:18px;">JOIN US IN OUR</div>
    <div class="t heavy" style="left:258px;top:44px;font-size:12px;">BOLD START CHALLENGE</div>
    <div class="dot-rule" style="left:180px;top:64px;width:155px;background:var(--pink);"></div>
    <div class="t light" style="left:258px;top:82px;font-size:19px;letter-spacing:1px;">NINETY DAYS</div>
    <div class="t heavy pink" style="left:258px;top:118px;font-size:42px;text-shadow:0 0 6px var(--glow);">BOLD</div>
    <div class="t bold" style="left:258px;top:152px;font-size:14px;">LOSE 20 POUNDS IN</div>
    <div class="t heavy pink" style="left:258px;top:200px;font-size:68px;text-shadow:0 0 8px var(--glow);">SIX</div>
    <div class="t light" style="left:258px;top:261px;font-size:37px;">WEEKS</div>
    <div class="dot-rule" style="left:180px;top:290px;width:155px;background:var(--pink);"></div>
    <div class="t heavy" style="left:258px;top:307px;font-size:17px;">BEGINS</div>
    <div class="t heavy" style="left:258px;top:328px;font-size:17px;">6 JANUARY 2025</div>
  </section>

  <!-- Graphic 5: text only on paper -->
  <section class="tile tile--e">
    <div class="band"></div>
    <div class="t heavy glow-pink" style="left:177px;top:35px;font-size:22px;">BOLD START CHALLENGE</div>
    <div class="t light" style="left:177px;top:84px;font-size:36px;letter-spacing:2px;">NINETY DAYS</div>
    <div class="t heavy" style="left:177px;top:147px;font-size:80px;">BOLD</div>
    <div class="t bold" style="left:177px;top:211px;font-size:24px;">LOSE 20 POUNDS IN</div>
    <div class="t heavy" style="left:177px;top:261px;font-size:36px;">SIX WEEKS</div>
    <div class="t heavy glow-pink" style="left:177px;top:326px;font-size:17px;">BEGINS 6 JANUARY 2025</div>
  </section>

  <!-- Graphic 6: phone with mirror photo, hot pink -->
  <section class="tile tile--f">
    <svg class="device" viewBox="0 0 150 307" aria-hidden="true">
      <rect x="1" y="1" width="148" height="305" rx="22" fill="#f4f4f4" stroke="#cfcfcf" stroke-width="2"/>
      <circle cx="52" cy="19" r="2.5" fill="#333"/>
      <rect x="62" y="17" width="28" height="3" rx="1.5" fill="#444"/>
      <circle cx="73" cy="286" r="11" fill="none" stroke="#9a9a9a" stroke-width="2"/>
    </svg>
    <div class="photo" role="img" aria-label="Smiling woman in a blue shirt measuring her waist in front of a mirror" style="left:9px;top:54px;width:138px;height:241px;background:linear-gradient(90deg,#ece8e2,#5a86bf 55%,#c9b9a6);"></div>
    <div class="t heavy" style="left:259px;top:26px;font-size:17px;">JOIN US IN OUR</div>
    <div class="t heavy" style="left:259px;top:43px;font-size:12px;">BOLD START CHALLENGE</div>
    <div class="dot-rule" style="left:183px;top:61px;width:152px;background:var(--white);"></div>
    <div class="t light" style="left:259px;top:80px;font-size:19px;letter-spacing:1px;">NINETY DAYS</div>
    <div class="t heavy" style="left:259px;top:117px;font-size:42px;text-shadow:0 0 6px var(--blush);">BOLD</div>
    <div class="t bold" style="left:259px;top:150px;font-size:14px;">LOSE 20 POUNDS IN</div>
    <div class="t heavy" style="left:256px;top:196px;font-size:68px;text-shadow:0 0 8px var(--blush);">SIX</div>
    <div class="t light" style="left:259px;top:255px;font-size:37px;">WEEKS</div>
    <div class="dot-rule" style="left:183px;top:281px;width:152px;background:var(--white);"></div>
    <div class="t heavy" style="left:259px;top:302px;font-size:17px;">BEGINS</div>
    <div class="t heavy" style="left:259px;top:323px;font-size:17px;">6 JANUARY 2025</div>
  </section>

</main>
</body>
</html>
```